Accident Law Firm Billboard Bold Easy to See Car Accidents

We need a billboard design that can catch attention in a very crowed Car Accident lawyer market. We wish to feature the phone number (652) 318-4470 as the focus of the Bill Board. We are trying to get the phone number recognized and remembered by drivers. The law firm name is not as crucial to remember.
Basically, It's CAR ACCIDENT? Then (652) 318-4470. We are not married to any specific color scheme but it has to POP and catch attention.
So the Crucial elements are as follows:
1. Phone number (652) 318-4470
2. Words CAR ACCIDENT?
3. Firm Logo in lower portion or where appropriate. Firm Logo to be provided
4. We may want to try a Day Glow orange color, with White and Black added. An example of the color scheme shall be provided.
5. Possible "Catch Phrase" to be used, "Ring Us Now"
Target Market(s)
Orlando Florida Car Accident victims
Industry/Entity Type
Law Firm
Requirements
Must have
- Easy to see phone number (652) 318-4470
- Catch attention
Nice to have
- I would like to have the sign visible in bright sunlight and it not too hard to immediately know what phone number is for
Should not have
- too many words
- No bold enough
- confusing fonts
- Unclear fonts

```html
<!DOCTYPE html>
<html lang="en">
<head>
<meta charset="utf-8">
<title>Marlowe Law Firm P.C – Car Accident Billboard</title>
<link rel="stylesheet" href="https://fonts.googleapis.com/css2?family=Montserrat:wght@600;800;900&display=swap">
<style>
  :root {
    --stage: #2b2f2c;
    --board: #ffffff;
    --ink: #0d0d0d;
    --dayglow: #f04e30;
    --car-orange: #f07a2a;
    --car-yellow: #f6b51e;
  }
  html, body {
    margin: 0;
    padding: 0;
    width: 1200px;
    height: 686px;
    overflow: hidden;
    background: var(--stage);
  }
  .stage {
    position: relative;
    width: 1200px;
    height: 686px;
  }
  .billboard {
    position: absolute;
    left: 98px;
    top: 90px;
    width: 1004px;
    height: 506px;
    background: var(--board);
    overflow: hidden;
    font-family: "Montserrat", Arial, sans-serif;
  }
  .firm-name {
    position: absolute;
    left: 57px;
    top: 34px;
    margin: 0;
    color: var(--ink);
    font-weight: 600;
    line-height: 1;
  }
  .firm-name .firm-main {
    display: block;
    font-size: 46px;
    letter-spacing: 3px;
  }
  .firm-name .firm-sub {
    display: block;
    margin-top: 3px;
    font-size: 22px;
    letter-spacing: 5px;
  }
  .crash-illustration {
    position: absolute;
    left: 345px;
    top: 72px;
    width: 308px;
    height: 160px;
    border-radius: 10px;
    background: linear-gradient(100deg, var(--car-orange) 0%, var(--car-orange) 45%, var(--car-yellow) 55%, var(--car-yellow) 100%);
    opacity: 0.9;
  }
  .headline {
    position: absolute;
    left: 55px;
    top: 160px;
    margin: 0;
    color: var(--ink);
    font-weight: 900;
    font-size: 104px;
    line-height: 88px;
    letter-spacing: -2px;
  }
  .headline span { display: block; }
  .phone {
    position: absolute;
    left: 55px;
    top: 364px;
    margin: 0;
    color: var(--dayglow);
    font-weight: 600;
    font-size: 100px;
    line-height: 1;
    letter-spacing: 4px;
  }
  .slogan {
    position: absolute;
    right: 44px;
    top: 62px;
    margin: 0;
    color: var(--ink);
    font-weight: 800;
    font-size: 52px;
    line-height: 58px;
    text-align: right;
  }
  .slogan span { display: block; }
  .slogan-dot {
    position: absolute;
    left: 858px;
    top: 258px;
    width: 100px;
    height: 100px;
    border-radius: 50%;
    background: var(--dayglow);
  }
</style>
</head>
<body>
  <div class="stage">
    <main class="billboard">
      <h2 class="firm-name">
        <span class="firm-main">MARLOWE</span>
        <span class="firm-sub">LAW FIRM P.C</span>
      </h2>

      <div class="crash-illustration" role="img" aria-label="Illustration of an orange car and a yellow car colliding head-on with a burst above them"></div>

      <h1 class="headline">
        <span>CAR</span>
        <span>ACCIDENT?</span>
      </h1>

      <p class="phone">(652) 318-4470</p>

      <p class="slogan">
        <span>Ring</span>
        <span>Us</span>
        <span>Now</span>
      </p>
      <div class="slogan-dot" aria-hidden="true"></div>
    </main>
  </div>
</body>
</html>
```